Flier redesign

Sample fliers are attached from previous 2 years "Seasonal care 2018" and "2019 Seasonal Care" . Need an updated design for this year.

Possible images are attached to this brief. If you use the before/after pictures - you should use both of them. Use images attached to this brief or any from our website that you may prefer.

Colors

Designer to choose colors to be used in the design.

Requirements
Must have
• Colors should match our website theme. www.oakmerefieldgrounds.org
• Should be a "new" design, not just copying one of the prior year designs with a different image.
• Must be created in photoshop and file must be provided at the end.
• Text should be the same as 2019 version.

```html
<!DOCTYPE html>
<html lang="en">
<head>
<meta charset="utf-8">
<title>Oakmere Field Grounds – 2019 Landscaping Packages</title>
<link href="https://fonts.googleapis.com/css2?family=Oswald:wght@300;500;600&family=Lato:wght@400;700&display=swap" rel="stylesheet">
<style>
:root{
  --stage:#303030;
  --maroon:#7d2132;
  --maroon-panel:rgba(128,36,54,.93);
  --charcoal:#474747;
  --charcoal-deep:#3f3f3f;
  --mist:#d9d9d9;
  --white:#ffffff;
  --ink:#2f2f2f;
  --body:#4a4a4a;
  --title-grey:#3a3a3a;
}
*{box-sizing:border-box;margin:0;padding:0}
html,body{width:1200px;height:1200px;overflow:hidden;background:var(--stage)}
body{position:relative;font-family:'Lato',sans-serif}
.flier{position:absolute;top:276px;width:480px;height:685px;background:var(--white);overflow:hidden}
.flier--angled{left:93px}
.flier--column{left:638px}
.abs{position:absolute}
.brand{display:flex;align-items:center;gap:7px;color:var(--maroon);font-family:'Lato',sans-serif;font-weight:400;letter-spacing:.5px;white-space:nowrap}
.brand__dot{width:9px;height:9px;border-radius:50%;background:var(--maroon)}
.photo{display:block}
.headline{font-family:'Oswald',sans-serif;color:var(--white);line-height:1;white-space:nowrap}
.pkg-title{font-family:'Lato',sans-serif;font-weight:400;text-transform:uppercase;letter-spacing:.2px;line-height:1.1}
.pkg-sub{font-size:10.5px;line-height:1.3}
.list{list-style:none;font-size:7.5px;line-height:1.35}
.list li{position:relative;margin-bottom:3px}
.price-badge{position:absolute;width:52px;height:52px;border-radius:50%;background:var(--white);color:var(--maroon);font-family:'Oswald',sans-serif;text-align:center;box-shadow:0 2px 5px rgba(0,0,0,.35);padding-top:10px;line-height:1}
.price-badge small{display:block;font-size:8px;font-weight:300}
.price-badge b{font-size:17px;font-weight:600}
.note{font-size:7.5px;line-height:1.35}
.price{font-family:'Oswald',sans-serif;font-weight:600;font-size:20px;color:var(--maroon);line-height:1}
.price-row{display:flex;align-items:center;gap:6px}
.price-row .note{border-left:1px solid currentColor;padding-left:6px}

/* angled flier */
.flier--angled .headline{left:264px;top:20px}
.flier--angled .headline .l1{font-size:22px;font-weight:600;letter-spacing:.3px}
.flier--angled .headline .l2{font-size:42px;font-weight:300;letter-spacing:.5px;margin-top:1px}
.seasonal-box{left:240px;top:0;width:227px;height:304px;background:var(--charcoal);clip-path:polygon(0 0,100% 0,100% 276px,0 304px);box-shadow:0 0 8px rgba(0,0,0,.4)}
.flier--angled .dark{color:var(--white)}
.flier--angled .list li::before{content:"";position:absolute;left:-14px;top:3px;width:4px;height:4px;border-radius:50%;background:var(--maroon)}
.flier--angled .dark .list li::before{background:var(--white)}
.perpetual-box{left:240px;top:400px;width:227px;height:252px;background:var(--mist);clip-path:polygon(0 20px,100% 0,100% 100%,0 100%)}
.footer-band{left:0;bottom:0;width:480px;height:33px;background:var(--maroon);color:var(--white);font-size:9px;display:flex;align-items:center;justify-content:space-between;padding:0 60px 0 25px}
.footer-band span,.contact span{display:flex;align-items:center;gap:9px}

/* column flier */
.flier--column .headline{left:240px;top:19px;color:var(--title-grey);font-size:18px;font-weight:600;letter-spacing:0}
.panel{left:223px;top:53px;width:243px;height:632px;background:var(--maroon-panel);color:var(--white)}
.panel .sec{position:absolute;left:17px;right:6px}
.panel .list li::before{content:"";position:absolute;left:-25px;top:1px;width:9px;height:9px;border-radius:50%;background:var(--white)}
.divider{position:absolute;left:0;width:243px;height:10px}
.ground{left:0;top:596px;width:223px;height:89px;background:var(--charcoal-deep)}
.contact{left:14px;top:645px;color:var(--white);font-size:9px;line-height:1.6}
.flier--column .price{color:var(--white);font-size:21px}
.monthly{display:flex;flex-direction:column;font-family:'Oswald',sans-serif;line-height:1;font-size:11px;font-weight:500;white-space:nowrap}
.monthly small{display:block;font-family:'Lato',sans-serif;font-size:7px;font-weight:400;line-height:1;margin-top:1px}
</style>
</head>
<body>

<!-- Version A: angled layout -->
<article class="flier flier--angled">
  <div class="abs brand" style="left:14px;top:36px;font-size:17px"><span>Oakmere</span><span class="brand__dot"></span><span>Field Grounds</span></div>

  <svg class="abs photo" style="left:0;top:0" width="480" height="685" role="img" aria-label="Autumn maple trees with red and orange leaves over a green cemetery lawn">
    <defs>
      <linearGradient id="foliageA" x1="0" y1="0" x2="0" y2="1">
        <stop offset="0" stop-color="#8f2a1d"/>
        <stop offset=".55" stop-color="#b2461e"/>
        <stop offset=".8" stop-color="#6e5a32"/>
        <stop offset="1" stop-color="#7c9a4e"/>
      </linearGradient>
    </defs>
    <polygon points="0,118 480,40 480,390 0,470" fill="url(#foliageA)"/>
    <line x1="0" y1="118" x2="240" y2="80" stroke="#9a9a9a" stroke-width="4"/>
    <line x1="0" y1="472" x2="240" y2="430" stroke="#9a9a9a" stroke-width="3"/>
  </svg>

  <div class="abs seasonal-box"></div>
  <div class="abs headline"><div class="l1">2019 LANDSCAPING</div><div class="l2">PACKAGES</div></div>

  <section class="abs dark" style="left:267px;top:98px;width:195px">
    <h2 class="pkg-title" style="font-size:13px">Seasonal Care</h2>
    <p class="pkg-sub">seasonal landscaping grave care</p>
    <ul class="list" style="margin-top:10px"><li>weeding and trimming rservices on your gravesite approximately every 7 weeekduring thegrowing season mid april throught mid october</li></ul>
  </section>
  <div class="price-badge" style="left:267px;top:178px"><small>2 YEAR</small><b>$230</b></div>
  <div class="price-badge" style="left:332px;top:178px"><small>2 YEAR</small><b>$230</b></div>
  <div class="price-badge" style="left:400px;top:178px"><small>1 YEAR</small><b>$115</b></div>
  <p class="abs note" style="left:267px;top:238px;width:170px;color:var(--white)">multy year payment locks in current &nbsp;rates valid throught &nbsp;10/31/2019</p>

  <div class="abs perpetual-box"></div>

  <section class="abs" style="left:22px;top:496px;width:205px;color:var(--ink)">
    <h2 class="pkg-title" style="font-size:13px">Basic Care Endowment</h2>
    <p class="pkg-sub" style="color:var(--body);margin-top:2px">landscaping care forever for graves with no plantings</p>
    <ul class="list" style="margin-top:10px;color:var(--body)">
      <li>weeding and trimming rservices on your gravesite &nbsp;2 timesd per year. mid may and mid september</li>
      <li>monnument leveling</li>
      <li>payment ensure grave care forever</li>
    </ul>
    <div class="price-row" style="margin-top:12px;color:var(--body)"><span class="price">$230</span><span class="note">cal for single payment discoutnt<br>valid throught 10/31/2019</span></div>
  </section>

  <section class="abs" style="left:267px;top:444px;width:200px;color:var(--ink)">
    <h2 class="pkg-title" style="font-size:13px">Perpetual Care<br>Endowment</h2>
    <p class="pkg-sub" style="color:var(--body);margin-top:3px">landscaping care forever for graves with no plantings</p>
    <ul class="list" style="margin-top:10px;color:var(--body)">
      <li>weeding and trimming rservices on your gravesite approximately every 7 weeekduring thegrowing season mid april throught mid october</li>
      <li>monument leveling and cleaning</li>
      <li>payment ensure grave care forever</li>
      <li>fullbed of boxwood shrubs</li>
      <li>trust &nbsp;certificate</li>
    </ul>
    <div class="price-row" style="margin-top:10px;color:var(--body)"><span class="price">$297</span><span class="note">cal for single payment discoutnt<br>valid throught 10/31/2019</span></div>
  </section>

  <footer class="abs footer-band">
    <span><svg width="8" height="8" viewBox="0 0 10 10"><circle cx="5" cy="5" r="4.3" fill="none" stroke="#fff"/><path d="M1 5h8M5 .7c-2 2.5-2 6 0 8.6M5 .7c2 2.5 2 6 0 8.6" fill="none" stroke="#fff" stroke-width=".8"/></svg>www.oakmerefieldgrounds.org</span>
    <span><svg width="8" height="8" viewBox="0 0 10 10"><path d="M2 .5l2 2.3-1.2 1.4c.7 1.4 1.6 2.3 3 3l1.4-1.2 2.3 2-1.3 1.5C4.8 9.3.7 5.2.5 1.8z" fill="#fff"/></svg>(201) 555-0148</span>
  </footer>
</article>

<!-- Version B: column layout -->
<article class="flier flier--column">
  <div class="abs brand" style="left:12px;top:20px;font-size:14px"><span>Oakmere</span><span class="brand__dot"></span><span>Field Grounds</span></div>
  <h1 class="abs headline">2019 LANDSCAPING PACKAGES</h1>

  <div class="abs ground"></div>
  <svg class="abs photo" style="left:14px;top:53px" width="209" height="582" role="img" aria-label="Tall autumn maple tree with red leaves on a green cemetery lawn">
    <defs>
      <linearGradient id="foliageB" x1="0" y1="0" x2="0" y2="1">
        <stop offset="0" stop-color="#d8d8d4"/>
        <stop offset=".12" stop-color="#a63522"/>
        <stop offset=".55" stop-color="#a9401d"/>
        <stop offset=".75" stop-color="#8a5a2c"/>
        <stop offset=".85" stop-color="#6d8f4a"/>
        <stop offset="1" stop-color="#7fa352"/>
      </linearGradient>
    </defs>
    <rect width="209" height="582" fill="url(#foliageB)"/>
  </svg>

  <div class="abs panel">
    <section class="sec" style="top:15px">
      <h2 class="pkg-title" style="font-size:14px;margin-left:-2px">Seasonal Care</h2>
      <p class="pkg-sub" style="font-size:11.5px;margin-top:6px">seasonal landscaping grave care</p>
      <ul class="list" style="margin-top:3px;font-size:8.2px"><li>weeding and trimming rservices on your gravesite approximately every 7 weeekduring thegrowing season mid april throught mid october</li></ul>
    </section>
    <div class="price-badge" style="left:20px;top:97px;width:58px;height:58px;padding-top:13px"><small>3 YEAR</small><b>$345</b></div>
    <div class="price-badge" style="left:97px;top:97px;width:58px;height:58px;padding-top:13px"><small>2 YEAR</small><b>$230</b></div>
    <div class="price-badge" style="left:176px;top:97px;width:58px;height:58px;padding-top:13px"><small>1 YEAR</small><b>$115</b></div>
    <p class="abs note" style="left:17px;top:164px;width:215px;font-size:8.2px">multy year payment locks in current &nbsp;rates valid throught &nbsp;10/31/2019</p>

    <svg class="divider" style="top:205px" viewBox="0 0 243 10"><path d="M0 .5h122l6 8 6-8h109" fill="none" stroke="#fff"/></svg>

    <section class="sec" style="top:232px">
      <h2 class="pkg-title" style="font-size:14px">Basic Care Endowment</h2>
      <p class="pkg-sub" style="font-size:11.5px;margin-top:5px">landscaping care forever for graves with no plantings</p>
      <ul class="list" style="margin-top:6px;font-size:8.2px">
        <li>weeding and trimming rservices on your gravesite &nbsp;2 timesd per year. mid may and mid september</li>
        <li style="margin-top:6px">monnument leveling</li>
        <li style="margin-top:6px">payment ensure grave care forever</li>
      </ul>
      <div class="price-row" style="margin-top:6px">
        <span class="monthly">12 MONTHLY<small>PAYMENT OF</small></span>
        <span class="price">$230</span>
        <span class="note" style="border-left-style:dashed;font-size:8.2px">cal for single payment<br>discoutnt valid throught<br>10/31/2019</span>
      </div>
    </section>

    <svg class="divider" style="top:391px" viewBox="0 0 243 10"><path d="M0 .5h122l6 8 6-8h109" fill="none" stroke="#fff"/></svg>

    <section class="sec" style="top:418px">
      <h2 class="pkg-title" style="font-size:14px">Perpetual Care<br>Endowment</h2>
      <p class="pkg-sub" style="font-size:11.5px;margin-top:6px">landscaping care forever for graves with no plantings</p>
      <ul class="list" style="margin-top:4px;font-size:8.2px">
        <li>weeding and trimming rservices on your gravesite approximately every 7 weeekduring thegrowing season mid april throught mid october</li>
        <li style="margin-top:4px">monument leveling and cleaning</li>
        <li style="margin-top:4px">payment ensure grave care forever</li>
        <li style="margin-top:4px">fullbed of boxwood shrubs</li>
        <li style="margin-top:4px">trust &nbsp;certificate</li>
      </ul>
      <div class="price-row" style="margin-top:6px">
        <span class="monthly">12 MONTHLY<small>PAYMENT OF</small></span>
        <span class="price">$297</span>
        <span class="note" style="border-left-style:dashed;font-size:8.2px">cal for single payment<br>discoutnt valid throught<br>10/31/2019</span>
      </div>
    </section>
  </div>

  <div class="abs contact">
    <span><svg width="8" height="8" viewBox="0 0 10 10"><circle cx="5" cy="5" r="4.3" fill="none" stroke="#fff"/><path d="M1 5h8M5 .7c-2 2.5-2 6 0 8.6M5 .7c2 2.5 2 6 0 8.6" fill="none" stroke="#fff" stroke-width=".8"/></svg>www.oakmerefieldgrounds.org</span>
    <span><svg width="8" height="8" viewBox="0 0 10 10"><path d="M2 .5l2 2.3-1.2 1.4c.7 1.4 1.6 2.3 3 3l1.4-1.2 2.3 2-1.3 1.5C4.8 9.3.7 5.2.5 1.8z" fill="#fff"/></svg>(201) 555-0148</span>
  </div>
</article>

</body>
</html>
```